7 variations of an already existing packet design needed

i need 8 colour and flavour variations of a design that i have already in AI/PDF/PSD format

i need 7 colour variations of the packet with the names of the flavours incorporated onto the packaging itself.

the 7 colour/flavour variations i want are

pineapple
cherry
blueberry
bubblegum
strawberry
menthol
mango
Apple & Blackcurrant

Requirements
Must have
• Must use the original design and have different colour anf flavour variations as described in the brief.
Should not have
• Not be an original design

```html
<!DOCTYPE html>
<html lang="en">
<head>
<meta charset="utf-8">
<title>Royal Puff – Flavour Variations</title>
<link rel="stylesheet" href="https://fonts.googleapis.com/css2?family=Oswald:wght@500;700&display=swap">
<style>
  :root {
    --paper: #ffffff;
    --rule: #1a1a1a;
    --blackcurrant: #111111;
    --blueberry: #0c4a8a;
    --bubblegum: #d7135f;
    --cherry: #5b2741;
    --mango: #e3633b;
    --menthol: #1d5a27;
    --pineapple: #f9ae4d;
    --strawberry: #a9252f;
  }
  * { box-sizing: border-box; margin: 0; padding: 0; }
  html, body {
    width: 1200px;
    height: 2268px;
    overflow: hidden;
    background: var(--paper);
  }
  .sheet {
    position: relative;
    width: 1200px;
    height: 2268px;
    display: grid;
    grid-template-columns: 600px 600px;
    grid-template-rows: 565px 567px 565px 571px;
    border: 2px solid var(--rule);
    background: var(--paper);
  }
  .variant {
    position: relative;
    border-right: 2px solid var(--rule);
    border-bottom: 2px solid var(--rule);
    overflow: hidden;
  }
  .variant:nth-child(2n) { border-right: none; }
  .variant:nth-last-child(-n+2) { border-bottom: none; }

  .smoke {
    position: absolute;
    left: 110px;
    top: 70px;
    width: 380px;
    height: 470px;
    border-radius: 46% 54% 40% 60% / 38% 42% 58% 62%;
    background:
      radial-gradient(ellipse at 30% 40%, var(--ink) 0%, transparent 62%),
      radial-gradient(ellipse at 72% 30%, var(--ink) 0%, transparent 58%),
      radial-gradient(ellipse at 50% 85%, var(--ink) 0%, transparent 55%);
    opacity: 0.28;
  }

  .label {
    position: absolute;
    left: 0;
    right: 0;
    top: 190px;
    display: flex;
    flex-direction: column;
    align-items: center;
    gap: 18px;
    color: var(--ink);
    font-family: "Oswald", "Arial Narrow", sans-serif;
    text-transform: uppercase;
  }
  .brand {
    display: flex;
    align-items: center;
    gap: 14px;
  }
  .brand-dot {
    width: 26px;
    height: 26px;
    border-radius: 50%;
    background: var(--ink);
  }
  .brand-name {
    font-weight: 700;
    font-size: 66px;
    line-height: 1;
    letter-spacing: 3px;
  }
  .flavour {
    font-weight: 500;
    font-size: 30px;
    line-height: 1.15;
    letter-spacing: 1.5px;
    text-align: center;
  }

  .dimension {
    position: absolute;
    font-family: "Oswald", "Arial Narrow", sans-serif;
    font-weight: 500;
    font-size: 22px;
    color: var(--rule);
  }
  .dimension-width { left: 1012px; top: 566px; }
  .dimension-height {
    left: 586px;
    top: 820px;
    transform: rotate(-90deg);
    transform-origin: left top;
  }

  .v-blackcurrant { --ink: var(--blackcurrant); }
  .v-blueberry    { --ink: var(--blueberry); }
  .v-bubblegum    { --ink: var(--bubblegum); }
  .v-cherry       { --ink: var(--cherry); }
  .v-mango        { --ink: var(--mango); }
  .v-menthol      { --ink: var(--menthol); }
  .v-pineapple    { --ink: var(--pineapple); }
  .v-strawberry   { --ink: var(--strawberry); }
</style>
</head>
<body>
<main class="sheet">
  <section class="variant v-blackcurrant">
    <div class="smoke" role="img" aria-label="Flowing smoke swirl illustration in grey tones"></div>
    <div class="label">
      <div class="brand"><span class="brand-dot"></span><span class="brand-name">Royal Puff</span></div>
      <p class="flavour">Blackcurrant<br>&amp; Apple</p>
    </div>
  </section>
  <section class="variant v-blueberry">
    <div class="smoke" role="img" aria-label="Flowing smoke swirl illustration in blue tones"></div>
    <div class="label">
      <div class="brand"><span class="brand-dot"></span><span class="brand-name">Royal Puff</span></div>
      <p class="flavour">Blueberry</p>
    </div>
  </section>
  <section class="variant v-bubblegum">
    <div class="smoke" role="img" aria-label="Flowing smoke swirl illustration in pink tones"></div>
    <div class="label">
      <div class="brand"><span class="brand-dot"></span><span class="brand-name">Royal Puff</span></div>
      <p class="flavour">Bubblegum</p>
    </div>
  </section>
  <section class="variant v-cherry">
    <div class="smoke" role="img" aria-label="Flowing smoke swirl illustration in plum tones"></div>
    <div class="label">
      <div class="brand"><span class="brand-dot"></span><span class="brand-name">Royal Puff</span></div>
      <p class="flavour">Cherry</p>
    </div>
  </section>
  <section class="variant v-mango">
    <div class="smoke" role="img" aria-label="Flowing smoke swirl illustration in orange tones"></div>
    <div class="label">
      <div class="brand"><span class="brand-dot"></span><span class="brand-name">Royal Puff</span></div>
      <p class="flavour">Mango</p>
    </div>
  </section>
  <section class="variant v-menthol">
    <div class="smoke" role="img" aria-label="Flowing smoke swirl illustration in green tones"></div>
    <div class="label">
      <div class="brand"><span class="brand-dot"></span><span class="brand-name">Royal Puff</span></div>
      <p class="flavour">Menthol</p>
    </div>
  </section>
  <section class="variant v-pineapple">
    <div class="smoke" role="img" aria-label="Flowing smoke swirl illustration in golden yellow tones"></div>
    <div class="label">
      <div class="brand"><span class="brand-dot"></span><span class="brand-name">Royal Puff</span></div>
      <p class="flavour">Pineapple</p>
    </div>
  </section>
  <section class="variant v-strawberry">
    <div class="smoke" role="img" aria-label="Flowing smoke swirl illustration in red tones"></div>
    <div class="label">
      <div class="brand"><span class="brand-dot"></span><span class="brand-name">Royal Puff</span></div>
      <p class="flavour">Strawberry</p>
    </div>
  </section>
  <span class="dimension dimension-width">9 cm</span>
  <span class="dimension dimension-height">8.5 cm</span>
</main>
</body>
</html>
```